Business Card for Mortuary

We need a business card design for our mortuary. We are not the "traditional" mortuary and specialize in simple cremations and burials. We use a two sided card.

Industry/Entity Type

Funeral Home

Contact Information for Business Card

One side we would like to have with the general information of the mortuary:
Address: 4127 E. Larkspur Ave, Sun City, AZ 85399
Phone: 623-555-0142
email: hello@willowbendmortuary.example
website: willowbendmortuary.example

On the other side would like to have the information of employee:
Name: Mark T. Ellis
Email: mark@willowbendmortuary.example
Title: Funeral Director
Text: 602-555-0187

Font styles to use
Serif
Sans Serif

Requirements
Should not have
• Do not put any gothic images or things like a hearse or tombstone.

```html
<!DOCTYPE html>
<html lang="en">
<head>
<meta charset="utf-8">
<title>Willowbend Mortuary – Business Cards</title>
<link rel="stylesheet" href="https://fonts.googleapis.com/css2?family=Montserrat:wght@700&family=Roboto:wght@400;700&display=swap">
<style>
  :root {
    --backdrop: #cfcfcb;
    --card: #ffffff;
    --ink: #111111;
    --text: #333333;
    --green: #6cba45;
    --lime: #c4dd36;
    --edge: #7cc04a;
  }
  * { box-sizing: border-box; margin: 0; padding: 0; }
  html, body { width: 1200px; height: 801px; overflow: hidden; }
  body {
    background: var(--backdrop);
    font-family: "Roboto", Arial, sans-serif;
    color: var(--text);
    position: relative;
  }
  .card {
    position: absolute;
    top: 246px;
    width: 540px;
    height: 309px;
    background: var(--card);
    border-bottom: 3px solid var(--edge);
    box-shadow: 0 6px 18px rgba(0,0,0,.18);
    overflow: hidden;
  }
  .card--front { left: 40px; }
  .card--back { left: 620px; }

  .emblem-area { position: absolute; }
  .card--front .emblem-area { right: -40px; top: -30px; width: 260px; height: 260px; }
  .card--back .emblem-area { right: -30px; bottom: -60px; width: 270px; height: 270px; }

  .brand { position: absolute; display: flex; align-items: stretch; gap: 8px; }
  .card--front .brand { left: 40px; top: 100px; }
  .card--back .brand { left: 40px; top: 36px; }
  .brand__name {
    font-family: "Roboto", Arial, sans-serif;
    font-weight: 700;
    color: var(--ink);
    text-transform: uppercase;
    line-height: .95;
    font-size: 25px;
    letter-spacing: -.3px;
  }
  .card--back .brand__name { font-size: 21px; }
  .brand__tagline {
    border-left: 1px solid var(--green);
    padding-left: 7px;
    color: var(--green);
    font-size: 12.5px;
    line-height: 1.2;
  }
  .card--back .brand__tagline { font-size: 11px; }

  .contact { position: absolute; list-style: none; font-size: 12px; line-height: 1.45; }
  .card--front .contact { left: 120px; top: 178px; }
  .contact li { display: flex; align-items: center; gap: 6px; }
  .icon { width: 11px; height: 11px; fill: var(--green); flex: none; }

  .person { position: absolute; left: 40px; top: 178px; }
  .person__name {
    font-family: "Montserrat", Arial, sans-serif;
    font-weight: 700;
    font-size: 25px;
    color: var(--green);
    line-height: 1.1;
  }
  .person__title { font-size: 16px; margin-bottom: 4px; }
  .person .contact { position: static; font-size: 14px; line-height: 1.5; }
  .person .icon { width: 14px; height: 14px; }
</style>
</head>
<body>
<svg width="0" height="0" style="position:absolute" aria-hidden="true">
  <defs>
    <symbol id="icon-phone" viewBox="0 0 24 24"><path d="M6.6 10.8a15.1 15.1 0 0 0 6.6 6.6l2.2-2.2a1 1 0 0 1 1-.25 11.4 11.4 0 0 0 3.6.57 1 1 0 0 1 1 1V20a1 1 0 0 1-1 1A17 17 0 0 1 3 4a1 1 0 0 1 1-1h3.5a1 1 0 0 1 1 1c0 1.25.2 2.45.57 3.57a1 1 0 0 1-.25 1z"/></symbol>
    <symbol id="icon-mail" viewBox="0 0 24 24"><path d="M2 5h20v14H2zm2 2v.4l8 5.2 8-5.2V7zm0 2.8V17h16V9.8l-8 5.2z"/></symbol>
    <symbol id="icon-globe" viewBox="0 0 24 24"><path d="M12 2a10 10 0 1 0 0 20 10 10 0 0 0 0-20zm6.9 6h-2.9a15.6 15.6 0 0 0-1.4-3.6A8 8 0 0 1 18.9 8zM12 4c.8 1.2 1.5 2.5 1.9 4h-3.8c.4-1.5 1.1-2.8 1.9-4zM4.3 14a8 8 0 0 1 0-4h3.4a16 16 0 0 0 0 4zm.8 2h2.9c.3 1.3.8 2.5 1.4 3.6A8 8 0 0 1 5.1 16zM8 8H5.1a8 8 0 0 1 4.3-3.6C8.8 5.5 8.3 6.7 8 8zm4 12c-.8-1.2-1.5-2.5-1.9-4h3.8c-.4 1.5-1.1 2.8-1.9 4zm2.3-6H9.7a14 14 0 0 1 0-4h4.6a14 14 0 0 1 0 4zm.3 5.6c.6-1.1 1.1-2.3 1.4-3.6h2.9a8 8 0 0 1-4.3 3.6zm1.7-5.6a16 16 0 0 0 0-4h3.4a8 8 0 0 1 0 4z"/></symbol>
    <radialGradient id="emblem-tone" cx="40%" cy="40%" r="70%">
      <stop offset="0" stop-color="#c4dd36"/>
      <stop offset="1" stop-color="#6cba45"/>
    </radialGradient>
  </defs>
</svg>

<section class="card card--front" aria-label="Company side">
  <svg class="emblem-area" viewBox="0 0 100 100" role="img" aria-label="Green leaf emblem area">
    <circle cx="50" cy="50" r="50" fill="url(#emblem-tone)" opacity=".85"/>
  </svg>
  <div class="brand">
    <div class="brand__name">Willowbend<br>Mortuary</div>
    <div class="brand__tagline">Affordable<br>Cremation<br>and Burial</div>
  </div>
  <ul class="contact">
    <li>4127 E. Larkspur Ave,</li>
    <li>Sun City, AZ 85399</li>
    <li><svg class="icon"><use href="#icon-phone"/></svg>623-555-0142</li>
    <li><svg class="icon"><use href="#icon-mail"/></svg>hello@willowbendmortuary.example</li>
    <li><svg class="icon"><use href="#icon-globe"/></svg>www.willowbendmortuary.example</li>
  </ul>
</section>

<section class="card card--back" aria-label="Employee side">
  <svg class="emblem-area" viewBox="0 0 100 100" role="img" aria-label="Green leaf emblem area">
    <circle cx="50" cy="50" r="50" fill="url(#emblem-tone)" opacity=".85"/>
  </svg>
  <div class="brand">
    <div class="brand__name">Willowbend<br>Mortuary</div>
    <div class="brand__tagline">Affordable<br>Cremation<br>and Burial</div>
  </div>
  <div class="person">
    <h1 class="person__name">Mark T. Ellis</h1>
    <p class="person__title">Funeral Director</p>
    <ul class="contact">
      <li><svg class="icon"><use href="#icon-phone"/></svg>602-555-0187</li>
      <li><svg class="icon"><use href="#icon-mail"/></svg>mark@willowbendmortuary.example</li>
    </ul>
  </div>
</section>
</body>
</html>
```